I am looking for a modern, clean and neat design for a reflexology and well being business. The business name is Mira Tellus (this is an old Latin word for wellbeing). The colours I would like are purple, white and grey. I am open to suggestions for pictures such as healing or working hands, a pair of feet, images that represent my business that you may think of....... or maybe you think no images at all would be best? My tag line is: "Relax, Renew, Revive" or "Find you balance......... Relax, Renew, Revive" I can decide which I want so I would like to see what both would look like. I would like space on the back to write the client's appointment date and time (more than once)

```html
<!DOCTYPE html>
<html lang="en">
<head>
<meta charset="utf-8">
<title>Mira Tellus – Business Card</title>
<link rel="stylesheet" href="https://fonts.googleapis.com/css2?family=Open+Sans:ital,wght@0,400;0,600;0,700;1,600;1,700&display=swap">
<style>
  :root {
    --purple: #9b0fb5;
    --ink: #3a3a3c;
    --grey: #555559;
    --rule: #b9b9bc;
    --paper: #ffffff;
    --paper-shade: #f1f1f2;
    --backdrop: #2b2c30;
  }
  * { box-sizing: border-box; margin: 0; padding: 0; }
  html, body { width: 1200px; height: 864px; overflow: hidden; }
  body {
    background: var(--backdrop);
    font-family: "Open Sans", Arial, sans-serif;
    position: relative;
  }
  .card {
    position: absolute;
    left: 320px;
    width: 560px;
    height: 320px;
    background: var(--paper);
    box-shadow: 0 10px 28px rgba(0,0,0,.45);
  }

  /* Appointment side */
  .appointment { top: 80px; }
  .appointment__title {
    position: absolute; top: 24px; left: 0; right: 0;
    text-align: center; color: var(--purple);
    font-weight: 700; font-size: 19px; line-height: 26px;
  }
  .field {
    position: absolute; display: flex; align-items: flex-end;
    color: var(--purple); font-weight: 600; font-size: 14px; line-height: 20px;
  }
  .field__line {
    flex: 1; margin-left: 6px; margin-bottom: 4px;
    border-bottom: 2px dotted var(--ink);
  }
  .field--name { top: 66px; left: 44px; width: 480px; }
  .slot { position: absolute; left: 44px; width: 480px; height: 20px; }
  .slot--first { top: 102px; }
  .slot--second { top: 136px; }
  .slot .field--date { top: 0; left: 0; width: 186px; }
  .slot .field--time { top: 0; left: 204px; width: 276px; }
  .field--time .ampm { margin-left: 6px; font-weight: 400; }
  .days {
    position: absolute; top: 174px; left: 40px; right: 40px;
    display: flex; justify-content: space-between; list-style: none;
  }
  .day {
    display: flex; align-items: center; gap: 6px;
    font-size: 12px; color: var(--grey);
  }
  .day__box {
    width: 20px; height: 16px; border: 2px solid var(--purple);
  }
  .notice {
    position: absolute; top: 212px; left: 0; right: 0; height: 56px;
    background: var(--purple); color: var(--paper);
    display: flex; align-items: center; justify-content: center;
    font-style: italic; font-weight: 700; font-size: 16px;
  }

  /* Contact side */
  .contact {
    top: 464px;
    background: linear-gradient(135deg, var(--paper-shade), var(--paper) 60%);
  }
  .brand {
    position: absolute; top: 52px; right: 48px;
    display: flex; align-items: center; gap: 16px;
    color: var(--ink); font-size: 40px; font-weight: 400; letter-spacing: .5px;
    line-height: 48px;
  }
  .brand__dot {
    width: 46px; height: 46px; border-radius: 50%; background: var(--ink);
  }
  .person { position: absolute; top: 132px; left: 40px; }
  .person__name { color: var(--purple); font-weight: 600; font-size: 20px; line-height: 1.1; }
  .person__role { color: var(--grey); font-size: 13px; }
  .divider {
    position: absolute; top: 162px; left: 190px; right: 48px;
    border-top: 1px solid var(--rule);
  }
  .tagline {
    position: absolute; left: 40px; bottom: 24px;
    color: var(--purple); font-style: italic; font-weight: 600;
    font-size: 15px; line-height: 20px;
  }
  .details {
    position: absolute; top: 196px; right: 40px;
    list-style: none; text-align: right;
    color: var(--ink); font-size: 15px; line-height: 22px;
  }
  .details li { display: flex; align-items: center; justify-content: flex-end; gap: 10px; }
  .details svg { width: 13px; height: 13px; fill: none; stroke: var(--purple); stroke-width: 2; }
</style>
</head>
<body>

<section class="card appointment">
  <h2 class="appointment__title">Your Next Appointment on</h2>
  <div class="field field--name">Name :<span class="field__line"></span></div>
  <div class="slot slot--first">
    <div class="field field--date">Date :<span class="field__line"></span></div>
    <div class="field field--time">Time :<span class="field__line"></span><span class="ampm">AM / PM</span></div>
  </div>
  <div class="slot slot--second">
    <div class="field field--date">Date :<span class="field__line"></span></div>
    <div class="field field--time">Time :<span class="field__line"></span><span class="ampm">AM / PM</span></div>
  </div>
  <ul class="days">
    <li class="day"><span class="day__box"></span>MON</li>
    <li class="day"><span class="day__box"></span>TUE</li>
    <li class="day"><span class="day__box"></span>WED</li>
    <li class="day"><span class="day__box"></span>THU</li>
    <li class="day"><span class="day__box"></span>FRI</li>
    <li class="day"><span class="day__box"></span>SAT</li>
  </ul>
  <p class="notice">If unable to keep appointment,&nbsp; kindly give 24hrs notice.</p>
</section>

<section class="card contact">
  <div class="brand"><span class="brand__dot"></span>Mira Tellus</div>
  <div class="person">
    <p class="person__name">Daniel Hart</p>
    <p class="person__role">Managing Director</p>
  </div>
  <div class="divider"></div>
  <p class="tagline">Relax, Renew, Revive</p>
  <ul class="details">
    <li>021-555-0148
      <svg viewBox="0 0 16 16"><path d="M3 2h3l1.5 3.5-2 1.2a8 8 0 0 0 3.8 3.8l1.2-2L14 10v3a1 1 0 0 1-1 1A11 11 0 0 1 2 3a1 1 0 0 1 1-1z"/></svg></li>
    <li>555-301-2746
      <svg viewBox="0 0 16 16"><rect x="2" y="6" width="12" height="8" rx="1"/><path d="M5 6V2h6v4M5 9h6M5 11.5h6"/></svg></li>
    <li>555-302-8819
      <svg viewBox="0 0 16 16"><rect x="4" y="1.5" width="8" height="13" rx="1.5"/><path d="M7 12h2"/></svg></li>
    <li>hello@miratellus.com
      <svg viewBox="0 0 16 16"><rect x="1.5" y="3.5" width="13" height="9" rx="1"/><path d="M2 4l6 5 6-5"/></svg></li>
    <li>www.miratellus.com
      <svg viewBox="0 0 16 16"><path d="M7 9l2-2M6 6.5 4 8.5a2.5 2.5 0 0 0 3.5 3.5l2-2M10 9.5l2-2A2.5 2.5 0 0 0 8.5 4l-2 2"/></svg></li>
  </ul>
</section>

</body>
</html>
```